Professional business cards for real estate development company

I need business cards for my new real estate development company. The company, "KORVA" is a real estate development, investment, and advisory firm with a focus on multifamily, office, and mixed-use projects across primary and secondary markets in the Southeast United States.

Style preference is modern

Industry/Entity Type

Real Estate Development

Contact Information for Business Card

The business cards need to include:
Name
Title
Mailing Address
Phone Number
Web Address

Logo is attached. I would like white to be the primary color with incorporation of the company colors: #232D3A and #B5A451

Font styles to use
Other font styles liked:
• Montserrat, Avenir

Requirements
Must have
• Company Logo. No need to include the company name since the name is in the logo.
Should not have
• No line type designs

```html
<!DOCTYPE html>
<html lang="en">
<head>
<meta charset="utf-8">
<title>KORVA Business Card</title>
<link rel="stylesheet" href="https://fonts.googleapis.com/css2?family=Montserrat:wght@400;500;600&display=swap">
<style>
  :root {
    --backdrop: #e3e5e8;
    --paper: #ffffff;
    --navy: #232d3a;
    --gold: #b5a451;
    --slate: #44556e;
    --cream: #fbf3cf;
    --butter: #f4e08a;
  }
  * { margin: 0; padding: 0; box-sizing: border-box; }
  html, body {
    width: 1200px;
    height: 1200px;
    overflow: hidden;
    background: var(--backdrop);
    font-family: "Montserrat", sans-serif;
  }
  .canvas {
    position: relative;
    width: 1200px;
    height: 1200px;
  }
  .card {
    position: absolute;
    top: 183px;
    width: 476px;
    height: 834px;
    background: var(--paper);
    overflow: hidden;
    box-shadow: 0 4px 14px rgba(0, 0, 0, 0.14);
  }
  .card--front { left: 80px; }
  .card--back { left: 644px; }

  .wordmark {
    position: absolute;
    left: 0;
    width: 100%;
    display: flex;
    justify-content: center;
    align-items: center;
    gap: 10px;
    font-weight: 600;
    letter-spacing: 0.06em;
    line-height: 1;
  }
  .wordmark__square {
    display: block;
    background: currentColor;
  }
  .card--front .wordmark {
    top: 70px;
    color: var(--navy);
    font-size: 24px;
  }
  .card--front .wordmark__square { width: 16px; height: 16px; }
  .card--back .wordmark {
    top: 392px;
    color: var(--gold);
    font-size: 50px;
    gap: 16px;
  }
  .card--back .wordmark__square { width: 34px; height: 34px; }

  .identity {
    position: absolute;
    top: 164px;
    width: 100%;
    text-align: center;
    color: var(--navy);
  }
  .identity__name {
    font-size: 33px;
    font-weight: 600;
    line-height: 1.1;
  }
  .identity__title {
    font-size: 26px;
    font-weight: 400;
    line-height: 1.25;
  }

  .contact {
    position: absolute;
    top: 268px;
    width: 100%;
    list-style: none;
    text-align: center;
    color: var(--navy);
    font-size: 19px;
    line-height: 30px;
  }
  .contact__item {
    display: flex;
    justify-content: center;
    align-items: center;
    gap: 10px;
  }
  .contact__icon {
    flex: none;
    width: 16px;
    height: 16px;
    fill: none;
    stroke: var(--navy);
    stroke-width: 1.6;
    stroke-linejoin: round;
  }

  .feature-art {
    position: absolute;
    left: 0;
    bottom: 0;
    width: 476px;
    height: 380px;
    background: linear-gradient(110deg, var(--slate) 0%, var(--slate) 36%, var(--cream) 38%, var(--butter) 78%);
  }

  .website {
    position: absolute;
    bottom: 26px;
    width: 100%;
    text-align: center;
    color: var(--navy);
    font-size: 21px;
    font-weight: 400;
  }
</style>
</head>
<body>
<main class="canvas">
  <section class="card card--front">
    <div class="wordmark"><span class="wordmark__square"></span>KORVA</div>

    <div class="identity">
      <h1 class="identity__name">Mara Lind</h1>
      <p class="identity__title">Managing Director</p>
    </div>

    <ul class="contact">
      <li class="contact__item">
        <svg class="contact__icon" viewBox="0 0 16 16" aria-hidden="true">
          <path d="M3 1.5 L6 1.5 L7 5 L5.2 6.2 C6 8 7.8 9.9 9.7 10.8 L10.9 9 L14.5 10 L14.5 13 C14.5 14 13.5 14.6 12.5 14.4 C7 13.4 2.6 9 1.6 3.5 C1.4 2.5 2 1.5 3 1.5 Z"/>
        </svg>
        <span>404-555-0187</span>
      </li>
      <li class="contact__item">
        <svg class="contact__icon" viewBox="0 0 16 16" aria-hidden="true">
          <rect x="1.5" y="3.5" width="13" height="9"/>
          <path d="M1.5 3.5 L8 9 L14.5 3.5"/>
        </svg>
        <span>maralind@korva.com</span>
      </li>
      <li class="contact__item">
        <svg class="contact__icon" viewBox="0 0 16 16" aria-hidden="true">
          <path d="M8 15 C8 15 3 9.5 3 6 A5 5 0 0 1 13 6 C13 9.5 8 15 8 15 Z"/>
          <circle cx="8" cy="6" r="1.8"/>
        </svg>
        <span>410 Magnolia Ave, Atlanta, GA</span>
      </li>
    </ul>

    <div class="feature-art" role="img" aria-label="Geometric building graphic in slate blue, cream and soft yellow"></div>
  </section>

  <section class="card card--back">
    <div class="wordmark"><span class="wordmark__square"></span>KORVA</div>
    <p class="website">www.korva.com</p>
  </section>
</main>
</body>
</html>
```